Quorvane - corporate Business Card

We need a good look and innovative business card for a new start up company based in Los Angeles called "Quorvane". We are in a payment business, including payment card, app, and ewallet. We are expert in online payment and Card not present (CNP) transaction.
We need an innovative, modern business card.

Our logo font is Aero Matics

Target Market(s)

Startup - Bank - Online Payment - Card Manufacturing

Industry/Entity Type

Startup

Contact Information for Business Card

phone: 424 555 0173 - Address: 4270 Marbrook blvd, Harlen Park, CA 90418

Requirements
Must have
• Message: innovative, professional, expert, high tech, trust, online payment expert, security
Nice to have
• no comment
Should not have
• no Comment

```html
<!DOCTYPE html>
<html lang="en">
<head>
<meta charset="utf-8">
<title>Quorvane Business Card</title>
<link href="https://fonts.googleapis.com/css2?family=Saira:wght@400;700&family=Roboto:wght@400;500&display=swap" rel="stylesheet">
<style>
  :root {
    --brand-red: #b81d2e;
    --brand-red-deep: #9c1c28;
    --paper: #ffffff;
    --ink: #2a2a2a;
    --stage: #6b7378;
  }
  * { margin: 0; padding: 0; box-sizing: border-box; }
  html, body { width: 1200px; height: 900px; overflow: hidden; }
  body {
    background: var(--stage);
    display: flex;
    align-items: center;
    justify-content: center;
    gap: 50px;
    font-family: "Roboto", sans-serif;
  }
  .card {
    position: relative;
    width: 530px;
    height: 303px;
    overflow: hidden;
    box-shadow: 0 14px 30px rgba(0,0,0,0.35);
  }

  /* Front side */
  .card-front { background: var(--brand-red); }
  .front-circle {
    position: absolute;
    width: 340px; height: 340px;
    left: 230px; top: 95px;
    border-radius: 50%;
    background: var(--brand-red-deep);
  }
  .front-brand {
    position: absolute;
    left: 38px; top: 72px;
    display: flex; align-items: center; gap: 16px;
  }
  .front-brand .brand-dot {
    width: 86px; height: 86px; border-radius: 50%;
    background: var(--paper);
  }
  .front-brand .brand-name {
    font-family: "Saira", sans-serif;
    font-weight: 700;
    font-size: 70px;
    color: var(--paper);
    letter-spacing: 1px;
    line-height: 1;
  }
  .front-web {
    position: absolute;
    left: 62px; top: 196px;
    font-size: 13px;
    color: var(--paper);
    letter-spacing: 0.3px;
  }

  /* Back side */
  .card-back { background: var(--paper); }
  .back-wave { position: absolute; left: 0; top: 0; }
  .back-brand {
    position: absolute;
    left: 24px; top: 58px;
    display: flex; align-items: center; gap: 8px;
  }
  .back-brand .brand-dot {
    width: 40px; height: 40px; border-radius: 50%;
    background: var(--brand-red);
  }
  .back-brand .brand-name {
    font-family: "Saira", sans-serif;
    font-weight: 700;
    font-size: 32px;
    color: var(--brand-red);
    line-height: 1;
  }
  .back-divider {
    position: absolute;
    left: 256px; top: 100px;
    width: 1px; height: 112px;
    background: var(--brand-red);
  }
  .contact {
    position: absolute;
    left: 270px; top: 100px;
    color: var(--ink);
    font-size: 11.5px;
    line-height: 1.35;
  }
  .contact .person {
    font-family: "Saira", sans-serif;
    font-size: 16px;
    color: var(--brand-red);
    line-height: 1.1;
  }
  .contact .person strong { font-weight: 700; }
  .contact .role { font-size: 11px; margin-bottom: 4px; }
  .contact .address { margin-bottom: 6px; }
  .contact-row { display: flex; align-items: center; gap: 6px; }
  .contact-row svg { width: 10px; height: 10px; flex: none; }
</style>
</head>
<body>

  <section class="card card-front" aria-label="Card front">
    <div class="front-circle"></div>
    <div class="front-brand">
      <span class="brand-dot"></span>
      <span class="brand-name">quorvane</span>
    </div>
    <p class="front-web">www.quorvane.com</p>
  </section>

  <section class="card card-back" aria-label="Card back">
    <svg class="back-wave" width="530" height="303" viewBox="0 0 530 303">
      <path d="M0 180 C40 215 260 275 530 300 L530 303 H0 Z" fill="var(--brand-red)"/>
      <path d="M0 168 C60 205 280 262 500 303 H488 C270 266 50 212 0 182 Z" fill="var(--paper)"/>
      <path d="M0 158 C70 200 290 258 470 303 H455 C270 258 50 205 0 170 Z" fill="var(--brand-red)"/>
    </svg>
    <div class="back-brand">
      <span class="brand-dot"></span>
      <span class="brand-name">quorvane</span>
    </div>
    <div class="back-divider"></div>
    <div class="contact">
      <p class="person"><strong>DERRIN</strong> CALLOWAY</p>
      <p class="role">FOUNDER</p>
      <p class="address">4270 Marbrook blvd<br>Harlen Park, CA 90418</p>
      <p class="contact-row">
        <svg viewBox="0 0 10 10"><path d="M2 0.5 L3.6 2.6 L2.6 3.6 C3.3 5 4.9 6.7 6.4 7.4 L7.4 6.4 L9.5 8 L8.3 9.5 C4.5 9 1 5.5 0.5 1.7 Z" fill="var(--brand-red)"/></svg>
        424 555 0173
      </p>
      <p class="contact-row">
        <svg viewBox="0 0 10 10"><rect x="2.5" y="0.5" width="5" height="9" rx="1" fill="none" stroke="var(--brand-red)"/></svg>
        000-000-0000
      </p>
      <p class="contact-row">
        <svg viewBox="0 0 10 10"><rect x="0.5" y="2" width="9" height="6.5" fill="var(--brand-red)"/><path d="M0.5 2 L5 6 L9.5 2" fill="none" stroke="var(--paper)" stroke-width="0.8"/></svg>
        hello@quorvane.com
      </p>
      <p class="contact-row">
        <svg viewBox="0 0 10 10"><circle cx="5" cy="5" r="4.5" fill="var(--brand-red)"/><path d="M0.5 5 H9.5 M5 0.5 C2.5 3 2.5 7 5 9.5 M5 0.5 C7.5 3 7.5 7 5 9.5" fill="none" stroke="var(--paper)" stroke-width="0.6"/></svg>
        www.quorvane.com
      </p>
    </div>
  </section>

</body>
</html>
```